Business Card Re-design

We are looking for a fresh bold look for general office business cards. We are a staffing agency that staffs industrial, coal mining, and clerical jobs.
Tag Line: We connect the RIGHT people with the RIGHT jobs.
Evansville Office: 2473 W. Tallow Creek Rd, Evansville, IN - 47308
p. 555.203.6180 f. 555.203.6195
Princeton Office: 264 S. Birch Ln, Princeton, IN - 47152
p. 555.319.2047 f. 555.203.6195
Absentee/Emergency 24hr Hotline 555.203.6172 opt.1
www.bluelanternworkforce.example

```html
<!DOCTYPE html>
<html lang="en">
<head>
<meta charset="utf-8">
<title>Blue Lantern Workforce – Business Cards</title>
<link href="https://fonts.googleapis.com/css2?family=Oswald:wght@400;500;600&display=swap" rel="stylesheet">
<style>
  :root {
    --backdrop: #6a8a48;
    --card: #f8f8fa;
    --navy: #1f3a6b;
    --green: #5aa545;
  }
  * { margin: 0; padding: 0; box-sizing: border-box; }
  html, body { width: 1200px; height: 1000px; overflow: hidden; }
  body {
    background: var(--backdrop);
    font-family: "Oswald", "Arial Narrow", sans-serif;
    color: var(--navy);
    position: relative;
  }
  .card {
    position: absolute;
    left: 248px;
    width: 704px;
    height: 402px;
    background: var(--card);
    box-shadow: 0 10px 30px rgba(0,0,0,0.25);
  }
  .card--front { top: 79px; }
  .card--back { top: 527px; }

  .brand-name {
    font-weight: 600;
    color: var(--navy);
    text-transform: uppercase;
    line-height: 1.02;
    letter-spacing: 0.5px;
  }
  .front-brand {
    position: absolute; left: 0; right: 0; top: 112px;
    text-align: center; font-size: 40px;
  }
  .front-tagline {
    position: absolute; left: 0; right: 0; top: 238px;
    text-align: center; font-size: 19px; color: var(--navy);
  }
  .accent { color: var(--green); }
  .front-url {
    position: absolute; left: 0; right: 0; top: 266px;
    text-align: center; font-size: 17px; color: var(--green);
  }

  .back-brand {
    position: absolute; left: 36px; top: 42px; font-size: 24px;
  }
  .back-url {
    position: absolute; left: 36px; top: 119px; font-size: 13px; color: var(--navy);
  }
  .hotline {
    position: absolute; right: 42px; top: 43px; text-align: right;
  }
  .hotline-title { font-size: 16px; color: var(--green); letter-spacing: 0.3px; }
  .hotline-number { font-size: 16px; color: var(--navy); margin-top: 2px; }

  .office { position: absolute; top: 184px; }
  .office--evansville { left: 34px; }
  .office--princeton { right: 34px; }
  .office-label {
    position: absolute; top: 0;
    writing-mode: vertical-rl;
    font-size: 16px; color: var(--green); letter-spacing: 1.5px;
    height: 100px; text-align: center;
  }
  .office--evansville .office-label { left: 0; transform: rotate(180deg); }
  .office--princeton .office-label { right: 0; }
  .office-lines { list-style: none; font-size: 17px; line-height: 1.2; }
  .office--evansville .office-lines { margin-left: 32px; }
  .office--princeton .office-lines { margin-right: 32px; text-align: right; }
  .office-lines li { display: flex; align-items: flex-start; gap: 10px; margin-bottom: 6px; }
  .office--princeton .office-lines li { flex-direction: row-reverse; }
  .icon { width: 16px; height: 16px; flex: none; margin-top: 3px; fill: var(--green); }

  .back-tagline {
    position: absolute; left: 0; right: 0; bottom: 28px;
    text-align: center; font-size: 20px; text-transform: uppercase; color: var(--navy);
  }
  .back-tagline .accent { font-weight: 600; }
</style>
</head>
<body>
  <svg width="0" height="0" style="position:absolute">
    <defs>
      <symbol id="icon-phone" viewBox="0 0 16 16"><path d="M3.6 1.2 5.8 1l1.2 3.4-1.6 1.2a8 8 0 0 0 5 5l1.2-1.6 3.4 1.2-.2 2.2c-.1.8-.8 1.4-1.6 1.4C6.4 13.8 2.2 9.6 2.2 2.8c0-.8.6-1.5 1.4-1.6z"/></symbol>
      <symbol id="icon-fax" viewBox="0 0 16 16"><path d="M1 5h2v10H1zM4 1h7l2 2v3h2v9H4zm2 2v3h5V4zm0 6v1.5h2V9zm3 0v1.5h2V9zm3 0v1.5h1.5V9zM6 12v1.5h2V12zm3 0v1.5h2V12z"/></symbol>
      <symbol id="icon-pin" viewBox="0 0 16 16"><path d="M8 0a5.5 5.5 0 0 0-5.5 5.5C2.5 10 8 16 8 16s5.5-6 5.5-10.5A5.5 5.5 0 0 0 8 0zm0 7.8a2.3 2.3 0 1 1 0-4.6 2.3 2.3 0 0 1 0 4.6z"/></symbol>
    </defs>
  </svg>

  <section class="card card--front">
    <div class="brand-name front-brand">Blue Lantern<br>Workforce</div>
    <p class="front-tagline">We connect the <span class="accent">RIGHT</span> people with the <span class="accent">RIGHT</span> jobs</p>
    <p class="front-url">www.bluelanternworkforce.example</p>
  </section>

  <section class="card card--back">
    <div class="brand-name back-brand">Blue Lantern<br>Workforce</div>
    <p class="back-url">www.bluelanternworkforce.example</p>

    <div class="hotline">
      <p class="hotline-title">ABSENTEE/EMERGENCY 24HR HOTLINE</p>
      <p class="hotline-number"><svg class="icon" style="vertical-align:-2px;margin:0 4px 0 0"><use href="#icon-phone"/></svg>555.203.6172 (opt.1)</p>
    </div>

    <div class="office office--evansville">
      <span class="office-label">EVANSVILLE</span>
      <ul class="office-lines">
        <li><svg class="icon"><use href="#icon-phone"/></svg><span>555.203.6180</span></li>
        <li><svg class="icon"><use href="#icon-fax"/></svg><span>555.203.6195</span></li>
        <li><svg class="icon"><use href="#icon-pin"/></svg><span>2473 W. Tallow Creek Rd,<br>Evansville, IN - 47308</span></li>
      </ul>
    </div>

    <div class="office office--princeton">
      <span class="office-label">PRINCETON</span>
      <ul class="office-lines">
        <li><svg class="icon"><use href="#icon-phone"/></svg><span>555.319.2047</span></li>
        <li><svg class="icon"><use href="#icon-fax"/></svg><span>555.203.6195</span></li>
        <li><svg class="icon"><use href="#icon-pin"/></svg><span>264 S. Birch Ln,<br>Princeton, IN - 47152</span></li>
      </ul>
    </div>

    <p class="back-tagline">We connect the <span class="accent">Right</span> people with the <span class="accent">Right</span> jobs</p>
  </section>
</body>
</html>
```